Business Card Design

Online clothing womens clothing store, I sell my clothing online and at the markets.

i would like the attached picture on the front of the card and the contact information on the back.

Industry/Entity Type

Business

Contact Information for Business Card

Harbor Thistle
Maren Pilcott
(Instagram symbol) _harbor_thistle_
(Facebook symbol) www.facebook.com/harborthistleau/

W : www.harborthistle.com.au
E : info@harborthistle.com.au
P : 0478614203

```html
<!DOCTYPE html>
<html lang="en">
<head>
<meta charset="utf-8">
<title>Harbor Thistle – Business Card</title>
<link rel="stylesheet" href="https://fonts.googleapis.com/css2?family=Barlow:wght@400&family=Cabin:wght@400;600&display=swap">
<style>
  :root {
    --ink: #000000;
    --paper: #ffffff;
    --backdrop: #e9e7e4;
    --photo-light: #dfe5e8;
    --photo-mid: #9fb1b8;
    --photo-dark: #3a3b3e;
  }
  * { margin: 0; padding: 0; box-sizing: border-box; }
  html, body {
    width: 1200px; height: 902px; overflow: hidden;
    background: var(--backdrop);
  }
  .card {
    position: absolute; left: 90px; top: 136px;
    width: 1020px; height: 630px;
    background: var(--paper);
    box-shadow: 0 6px 24px rgba(0,0,0,0.18);
  }
  .top-band {
    position: absolute; left: 70px; top: 0;
    width: 851px; height: 90px;
    background: var(--ink);
  }
  .wordmark {
    position: absolute; left: 70px; top: 158px;
    width: 851px; text-align: center;
    font-family: "Barlow", sans-serif; font-weight: 400;
    font-size: 72px; line-height: 80px;
    letter-spacing: 0.17em; color: var(--ink);
    white-space: nowrap;
  }
  .contact-panel {
    position: absolute; left: 70px; top: 314px;
    width: 436px; height: 316px;
    background: var(--ink); color: var(--paper);
    font-family: "Cabin", sans-serif;
  }
  .person-name {
    position: absolute; left: 26px; top: 14px;
    font-size: 34px; font-weight: 600; line-height: 38px;
  }
  .person-role {
    position: absolute; left: 27px; top: 55px;
    font-size: 23px; font-weight: 400; line-height: 26px;
  }
  .contact-list {
    position: absolute; left: 21px; top: 128px;
    list-style: none;
  }
  .contact-list li {
    display: flex; align-items: center;
    height: 33px; font-size: 26px; line-height: 33px;
  }
  .contact-list svg { width: 28px; height: 28px; margin-right: 8px; flex: none; }
  .photo-area {
    position: absolute; left: 517px; top: 314px;
    width: 404px; height: 316px;
    background: linear-gradient(110deg, var(--photo-light) 0%, var(--photo-mid) 50%, var(--photo-dark) 100%);
  }
  .side-strip {
    position: absolute; left: 932px; top: 0;
    width: 88px; height: 630px;
    background: var(--ink);
  }
  .side-strip .website {
    position: absolute; left: 50%; top: 50%;
    transform: translate(-50%, -50%) rotate(-90deg);
    font-family: "Cabin", sans-serif; font-size: 25px;
    color: var(--paper); white-space: nowrap;
  }
</style>
</head>
<body>
  <div class="card">
    <div class="top-band"></div>
    <div class="wordmark">HARBOR THISTLE</div>

    <div class="contact-panel">
      <div class="person-name">Maren Pilcott</div>
      <div class="person-role">Managing Director</div>
      <ul class="contact-list">
        <li>
          <svg viewBox="0 0 28 28" aria-hidden="true">
            <rect x="2" y="3" width="24" height="22" rx="3" fill="#fff"/>
            <path d="M7 10c0-2 2-3 7-3s7 1 7 3v2h-4v-2h-6v2H7z" fill="#000"/>
            <rect x="9" y="14" width="10" height="8" rx="1" fill="#000"/>
          </svg>0478614203
        </li>
        <li>
          <svg viewBox="0 0 28 28" aria-hidden="true">
            <rect x="3" y="6" width="22" height="17" fill="none" stroke="#fff" stroke-width="2.2"/>
            <path d="M3 6l11 10 11-10M3 23l8-8M25 23l-8-8" fill="none" stroke="#fff" stroke-width="2"/>
          </svg>info@harborthistle.com.au
        </li>
        <li>
          <svg viewBox="0 0 28 28" aria-hidden="true">
            <rect x="4" y="4" width="20" height="20" fill="#fff"/>
          </svg>_harbor_thistle_
        </li>
        <li>
          <svg viewBox="0 0 28 28" aria-hidden="true">
            <rect x="4" y="4" width="20" height="20" fill="#fff"/>
          </svg>harborthistleau
        </li>
      </ul>
    </div>

    <div class="photo-area" role="img" aria-label="Misty fashion photograph of a model in soft grey-blue tones"></div>

    <div class="side-strip">
      <span class="website">www.harborthistle.com.au</span>
    </div>
  </div>
</body>
</html>
```